Kerno Solutions: searching for a flyer to trow in letterboxes for properties we are interested in

Hello ,

Introduction:
We are a company based in Luxembourg called "Kerno Solutions". We are specialized in buying properties on which we develop and build constructions before selling them.

Informations for the flyer:
We need a flyer to trow into the letter boxes of property owners letting them know that we are interested in buying their property, if they are interested they can give us a call.

The text for the flyer/letter is in the attachment called >>2020-03-11_KS_Text for flyer,letter there might be slight changes<<.

We need to look competent, professional and financially stable.

The flyer needs to be short and not over welling with information otherwise it will land in the trash.

We have decided that we don't want real pictures on the flyer, but shapes of any kind, blue prints, drawings are fine.

Format should be in DIN A4. We plan to print the flyer on both sides in two different languages, in other words the design will be the same on both sides only the text will be in a different language.

I also added our current logo and here is the design of the website that is under construction at the moment http://www.kernosolutions-example.lu/. The logo's color can be changed into a different blue or uni color (all white or all black).
Updates

Hi, First time user the howl thing started faster as expected. Furthermore, I need to catch my boss to discust the project with him and he is on a lot of meetings. Please give us a little bit more time. Thanks

Target Market(s)

Property owners

Requirements
Must have
• email, phone number, tax number (RCS), Tax number , matriculation and address.
see word file in attachment for information
Nice to have
• Our company logo, in one form or an other, you can be creative, the logo is in the attachment.
Should not have
• Real pictures

```html
<!DOCTYPE html>
<html lang="fr">
<head>
<meta charset="utf-8">
<title>Kerno Solutions – Flyer recto verso</title>
<link rel="stylesheet" href="https://fonts.googleapis.com/css2?family=Oswald:wght@400;500&family=Open+Sans:wght@400;600;700&display=swap">
<style>
  :root{
    --backdrop:#747474;
    --navy:#1d3f6e;
    --navy-mid:#2d5a8c;
    --accent:#3fb3e8;
    --ink:#1c1c1c;
    --paper:#ffffff;
    --muted:#5a5a5a;
  }
  *{box-sizing:border-box;margin:0;padding:0}
  html,body{width:1200px;height:1200px;overflow:hidden;background:var(--backdrop)}
  .stage{position:relative;width:1200px;height:1200px}
  .flyer{
    position:absolute;top:226px;width:533px;height:748px;background:var(--paper);
    box-shadow:6px 8px 14px rgba(0,0,0,.35);overflow:hidden;
    font-family:"Open Sans",Arial,sans-serif;color:var(--ink);
  }
  .flyer--fr{left:46px}
  .flyer--lb{left:622px}
  .top-band{position:absolute;left:0;top:0;width:100%;height:15px;background:var(--navy)}
  .hero{
    position:absolute;left:0;top:15px;width:100%;height:300px;
    background:linear-gradient(180deg,#f2f4f2 0%,#dfe4e2 38%,#8a9aa6 58%,#4d5d6b 72%,#3b3a36 100%);
  }
  .title-band{
    position:absolute;left:0;top:315px;width:100%;height:92px;
    border-top:3px solid var(--accent);border-bottom:3px solid var(--accent);
    background:linear-gradient(90deg,var(--navy) 0%,var(--navy-mid) 50%,var(--navy) 100%);
    text-align:center;color:#fff;
  }
  .title-band h1{font-family:"Oswald",Arial,sans-serif;font-weight:400;font-size:40px;letter-spacing:.5px;line-height:1;margin-top:14px}
  .title-band p{font-weight:700;font-size:16px;margin-top:6px;letter-spacing:.3px}
  .letter{position:absolute;left:30px;right:24px;top:433px;font-size:10.3px;line-height:1.22}
  .letter .salutation{font-weight:700;margin-bottom:14px}
  .letter p{margin-bottom:12px}
  .letter .sign{margin-bottom:8px;padding-left:1px}
  .footer-band{
    position:absolute;left:0;bottom:0;width:100%;height:66px;
    background:linear-gradient(90deg,var(--navy) 0%,var(--navy-mid) 50%,var(--navy) 100%);
  }
  .footer-band .rcs{position:absolute;left:46px;top:33px;color:#e6eef7;font-size:10.5px}
  .footer-band .web{position:absolute;right:49px;top:33px;color:#e6eef7;font-size:10.5px}
  .contact-card{
    position:absolute;left:30px;top:616px;width:472px;height:90px;background:#fff;
    border-radius:8px;box-shadow:0 2px 6px rgba(0,0,0,.35);
  }
  .contact-card .phone{
    position:absolute;left:38px;top:10px;font-family:"Oswald",Arial,sans-serif;
    color:var(--accent);font-size:20px;letter-spacing:.5px
  }
  .contact-card .line{position:absolute;left:38px;font-size:10.5px;color:var(--ink)}
  .contact-card .email{top:45px}
  .contact-card .address{top:62px}
  .contact-card svg{position:absolute}
  .brand{
    position:absolute;right:24px;top:58px;font-family:"Oswald",Arial,sans-serif;
    font-weight:500;font-size:15px;color:var(--navy);letter-spacing:.2px;
  }
  .brand-mark{position:absolute;right:62px;top:16px;width:34px;height:34px;background:var(--navy)}
</style>
</head>
<body>
<main class="stage">

  <section class="flyer flyer--fr" lang="fr">
    <div class="top-band"></div>
    <div class="hero" role="img" aria-label="Photographie d'une maison moderne en pierre au bord d'un lac au coucher du soleil"></div>
    <header class="title-band">
      <h1>SITE EN CONSTRUCTION</h1>
      <p>Kerno Solutions s.à.r.l</p>
    </header>
    <article class="letter">
      <p class="salutation">Madame, Monsieur,</p>
      <p>Ce courrier vous a été adressé, car votre propriété a attiré notre attention. Nous souhaiterions discuter avec vous de son éventuel rachat par notre société.</p>
      <p>En cas d’accord, nous vous assurons une décision rapide, un paiement garanti, et zéro frais d’intermédiaire.</p>
      <p>En attendant de vos nouvelles, nous restons à votre entière disposition pour tout renseignement.</p>
      <p class="sign">Salutations distinguées,</p>
      <p class="sign">L’équipe de Kerno Solutions</p>
    </article>
    <div class="footer-band">
      <span class="rcs">tax number (RCS):</span>
      <span class="web">www.kernosolutions-example.lu</span>
    </div>
    <aside class="contact-card">
      <svg style="left:18px;top:16px" width="12" height="18" viewBox="0 0 12 18" aria-hidden="true"><path d="M4 1 L7 1 L6 5 L4 6 Q4 11 7 13 L9 12 L11 15 L8 17 Q2 15 1.5 8 Q1.5 3 4 1Z" fill="var(--accent)"/></svg>
      <span class="phone">691-000-482</span>
      <svg style="left:20px;top:47px" width="12" height="8" viewBox="0 0 12 8" aria-hidden="true"><rect width="12" height="8" rx="1" fill="var(--accent)"/><path d="M0.5 0.5 L6 5 L11.5 0.5" stroke="#fff" stroke-width="1" fill="none"/></svg>
      <span class="line email">info@kernosolutions-example.lu</span>
      <svg style="left:21px;top:62px" width="10" height="13" viewBox="0 0 10 13" aria-hidden="true"><path d="M5 12 Q1 7 1 4.5 A4 4 0 0 1 9 4.5 Q9 7 5 12Z" fill="none" stroke="var(--accent)" stroke-width="1.3"/><circle cx="5" cy="4.6" r="1.4" fill="var(--accent)"/></svg>
      <span class="line address">17 rue des Artisans, L-5610 Mondorf</span>
      <span class="brand-mark" aria-hidden="true"></span>
      <span class="brand">KERNO SOLUTIONS</span>
    </aside>
  </section>

  <section class="flyer flyer--lb" lang="lb">
    <div class="top-band"></div>
    <div class="hero" role="img" aria-label="Foto vun engem modernen Steenhaus um Séi bei der Sonnenënnergang"></div>
    <header class="title-band">
      <h1>SITE EN CONSTRUCTION</h1>
      <p>Kerno Solutions s.à.r.l</p>
    </header>
    <article class="letter">
      <p class="salutation">Madame, Monsieur,</p>
      <p>Dir kritt dëst Schreiwes well Är Proprietéit eis Opmierksamkeet zeréckbehalen huet.<br>Mir géinge gär mat Iech iwwert d’Méiglechkeet, datt eise Betrib se opkeeft, diskutéieren.</p>
      <p>Mir versécheren Iech e séieren Entscheedungsprozess, garantéieren d’Bezuelung a verrechne keng Drëttkäschten.</p>
      <p>Mir géingen eis freeën, vun Iech ze héieren, a sti ganz zu Ärer Verfügung fir zousätzlech Informatiounen.</p>
      <p class="sign">Mat beschte Gréiss,</p>
      <p class="sign">D’Equipe vun Kerno Solutions</p>
    </article>
    <div class="footer-band">
      <span class="rcs">tax number (RCS):</span>
      <span class="web">www.kernosolutions-example.lu</span>
    </div>
    <aside class="contact-card">
      <svg style="left:18px;top:16px" width="12" height="18" viewBox="0 0 12 18" aria-hidden="true"><path d="M4 1 L7 1 L6 5 L4 6 Q4 11 7 13 L9 12 L11 15 L8 17 Q2 15 1.5 8 Q1.5 3 4 1Z" fill="var(--accent)"/></svg>
      <span class="phone">691-000-482</span>
      <svg style="left:20px;top:47px" width="12" height="8" viewBox="0 0 12 8" aria-hidden="true"><rect width="12" height="8" rx="1" fill="var(--accent)"/><path d="M0.5 0.5 L6 5 L11.5 0.5" stroke="#fff" stroke-width="1" fill="none"/></svg>
      <span class="line email">info@kernosolutions-example.lu</span>
      <svg style="left:21px;top:62px" width="10" height="13" viewBox="0 0 10 13" aria-hidden="true"><path d="M5 12 Q1 7 1 4.5 A4 4 0 0 1 9 4.5 Q9 7 5 12Z" fill="none" stroke="var(--accent)" stroke-width="1.3"/><circle cx="5" cy="4.6" r="1.4" fill="var(--accent)"/></svg>
      <span class="line address">17 rue des Artisans, L-5610 Mondorf</span>
      <span class="brand-mark" aria-hidden="true"></span>
      <span class="brand">KERNO SOLUTIONS</span>
    </aside>
  </section>

</main>
</body>
</html>
```